Zolna Radio Web

Radio Station web site to include but not limited:

- About US (company profile)
- Now playing (from our streaming server link)
- Upcoming events with a possibility to have photos for advertisement purpose, etc...
- Language switch from Russian to English

- Member section:
Login module (with new user name and password, forgot password, etc...)
Login module with Chatterloop details
Request a song
LIKE feature with Chatterloop...

- Social links: (along with Chatterloop LIKE)
Send page to a friend
share / chatterloop share
Chat section where all logged users can chat in the same room.

- Contact us (Radio email ID )
- TabQuill - TuneBrick compatible

2 Websites were found to match the design that we re looking for:
http://www.vetrika.com and
http://marcotelvin.com

The site colors shall be matching and ongoing with our logo colors and designs as well.

Thanks,
Zolna Radio Team
Updates

Extended dead line and project is guaranteed.

Project Deadline Extended
Reason: Need more designs for review...

Industry/Entity Type

Radio

Requirements
Must have
• Chatterloop Login
Chatterloop LIKE
Users Chat Section
Language Switch
TabQuill - TuneBrick compatible
Nice to have
• Less pages switch. Initial shall be to switch from russian to english (or EN to RU) but the less pages we flip, the better. (except pop ups for log in, request a song, etc...)

```html
<!DOCTYPE html>
<html lang="en">
<head>
<meta charset="utf-8">
<title>Zolna Radio</title>
<link href="https://fonts.googleapis.com/css2?family=Montserrat:wght@300;400;600;700&family=Arimo:wght@400;700&display=swap" rel="stylesheet">
<style>
:root{
  --navy:#0d1a2c;
  --navy-deep:#050b14;
  --blue:#1d5fa8;
  --yellow:#f5b21a;
  --orange:#f39a1e;
  --orange-light:#fcc348;
  --white:#ffffff;
  --grey:#c9ccd2;
  --panel:rgba(0,0,0,0.82);
  --panel-dark:rgba(4,8,14,0.9);
  --footer:#050505;
}
*{margin:0;padding:0;box-sizing:border-box}
html,body{width:1200px;height:800px;overflow:hidden}
body{position:relative;background:var(--navy-deep);font-family:"Arimo",Arial,sans-serif;color:var(--white)}
.backdrop{position:absolute;inset:0;background:radial-gradient(ellipse at 50% 45%,#2b3c52 0%,#16233a 45%,#070d17 100%)}
.topbar{position:absolute;left:0;top:0;width:1200px;height:68px;background:linear-gradient(90deg,#02060c 0%,#071222 55%,#10284a 100%)}
.brand{position:absolute;left:36px;top:20px;display:flex;align-items:center;gap:8px;white-space:nowrap}
.brand-dot{width:30px;height:30px;border-radius:50%;background:var(--blue)}
.brand-name{font-family:"Montserrat",sans-serif;font-weight:700;font-size:14px;color:var(--yellow)}
.now-playing{position:absolute;left:170px;top:30px;display:flex;align-items:center;white-space:nowrap}
.now-playing .label{font-family:"Montserrat",sans-serif;font-weight:700;font-size:12px;color:var(--yellow);margin-left:8px}
.play-btn{margin-left:16px;width:20px;height:20px;background:#1b2f4e;display:flex;align-items:center;justify-content:center}
.track{margin-left:10px;font-family:"Montserrat",sans-serif;font-weight:600;font-size:12px}
.lang{position:absolute;left:921px;top:25px;display:flex;align-items:center;gap:8px;font-family:"Montserrat",sans-serif;font-weight:600;font-size:12px}
.lang svg{display:block}
.chat{position:absolute;left:1062px;top:23px;display:flex;align-items:center;gap:8px;font-family:"Montserrat",sans-serif;font-weight:600;font-size:12px}
.main{position:absolute;left:202px;top:196px;width:800px;height:452px;background:var(--panel)}
.event{position:absolute;left:11px;top:11px;width:526px;height:233px;background:linear-gradient(135deg,#1c2e6a 0%,#3d5fb3 45%,#1a2a55 75%,#4b1c3a 100%)}
.event-title{position:absolute;left:16px;top:179px;font-family:"Montserrat",sans-serif;font-weight:600;font-size:16px;color:var(--yellow)}
.event-sub{position:absolute;left:16px;top:206px;font-size:12px}
.event-more{position:absolute;left:440px;top:189px;font-family:"Montserrat",sans-serif;font-weight:700;font-style:italic;font-size:9px;color:var(--yellow)}
.dots{position:absolute;left:427px;top:212px;display:flex;gap:4px}
.dots span{width:9px;height:9px;background:#d7dbe3;border-radius:1px}
.dots span.on{background:var(--orange)}
.member{position:absolute;left:548px;top:11px;width:240px;height:233px;background:var(--panel-dark);padding:12px 17px}
h2{font-family:"Montserrat",sans-serif;font-weight:700;font-size:12px;color:var(--yellow)}
.field-label{font-weight:700;font-size:11px;margin:5px 0 2px 2px}
.field{display:block;width:204px;height:16px;background:var(--white)}
.login-row{display:flex;justify-content:space-between;align-items:center;margin-top:9px;font-size:10px;color:var(--grey)}
.btn-small{background:linear-gradient(#fdb73c,#f08a10);color:#1a1204;font-family:"Montserrat",sans-serif;font-weight:700;font-size:10px;padding:3px 7px;white-space:nowrap}
.btn-social{margin-top:16px;width:205px;height:33px;background:linear-gradient(#2b66b0,#143f7c);display:flex;align-items:center;font-size:13px;border-radius:2px;white-space:nowrap}
.btn-social .sq{width:14px;height:14px;background:var(--white);margin:0 10px 0 10px;flex:none}
.btn-social b{margin-left:4px}
.btn-signup{margin-top:14px;width:204px;height:25px;background:linear-gradient(var(--orange-light),var(--orange));color:#1a1204;font-family:"Montserrat",sans-serif;font-weight:700;font-size:12px;display:flex;align-items:center;justify-content:center}
.about{position:absolute;left:25px;top:266px;width:500px}
.about h1{font-family:"Montserrat",sans-serif;font-weight:300;font-size:16px}
.about h1 b{font-weight:600;color:var(--yellow)}
.contact{position:absolute;left:321px;top:268px;font-family:"Montserrat",sans-serif;font-weight:700;font-size:10px}
.contact a{color:var(--yellow);text-decoration:none;font-weight:600}
.about p{margin-top:14px;font-size:10.3px;line-height:15px;color:#e8e9ec}
.compat{position:absolute;left:22px;top:415px;font-family:"Montserrat",sans-serif;font-size:14px;display:flex;align-items:center;gap:5px;white-space:nowrap}
.compat .y{color:var(--yellow);font-weight:600}
.compat b{font-weight:700}
.compat-more{position:absolute;left:447px;top:417px;display:flex;align-items:center;gap:6px;font-family:"Montserrat",sans-serif;font-weight:700;font-style:italic;font-size:9px;color:var(--yellow)}
.side{position:absolute;left:565px;top:263px;width:210px}
.side p{font-size:9px;color:#e2e4e8;margin-top:3px;line-height:12px}
.form-row{display:flex;gap:7px;margin-top:14px;align-items:center}
.form-row .field{width:151px;height:16px}
.side .second{margin-top:27px}
.footer{position:absolute;left:0;top:752px;width:1200px;height:48px;background:var(--footer);display:flex;align-items:center}
.follow{margin-left:27px;font-family:"Montserrat",sans-serif;font-weight:700;font-size:10px;color:#9a9da3}
.wordmark{margin-left:16px;font-family:"Montserrat",sans-serif;font-weight:700;font-size:16px;color:#8a8d93}
.shares{position:absolute;right:18px;top:17px;display:flex;gap:14px}
.share{display:flex;align-items:center;gap:4px}
.share .b{font-size:9px;padding:2px 5px;border:1px solid #c8ccd4;background:#eef0f4;color:#2d4d86}
.share .b.orange{background:var(--orange);border-color:var(--orange);color:var(--white)}
.share .n{font-size:9px;font-weight:700;padding:2px 4px;background:var(--white);color:#222;border:1px solid #ccc}
</style>
</head>
<body>
<div class="backdrop" role="img" aria-label="Close-up photograph of a dark microphone grille"></div>

<header class="topbar">
  <div class="brand"><span class="brand-dot"></span><span class="brand-name">Zolna Radio</span></div>
  <div class="now-playing">
    <svg width="26" height="16" viewBox="0 0 26 16"><g fill="#f5b21a"><rect x="0" y="6" width="4" height="10"/><rect x="6" y="3" width="4" height="13"/><rect x="12" y="0" width="4" height="16"/><rect x="18" y="4" width="4" height="12"/><rect x="23" y="9" width="3" height="7"/></g></svg>
    <span class="label">NOW PLAYING</span>
    <span class="play-btn"><svg width="9" height="10" viewBox="0 0 9 10"><path d="M0 0L9 5L0 10Z" fill="#f5b21a"/></svg></span>
    <span class="track">Velvet Static - The Amber Lanterns</span>
  </div>
  <div class="lang">Language
    <svg width="25" height="16" viewBox="0 0 25 16"><rect width="25" height="5.33" fill="#fff"/><rect y="5.33" width="25" height="5.34" fill="#1d3fa0"/><rect y="10.67" width="25" height="5.33" fill="#d52b1e"/></svg>
    <svg width="25" height="16" viewBox="0 0 25 16"><rect width="25" height="16" fill="#1f3a8a"/><path d="M0 0L25 16M25 0L0 16" stroke="#fff" stroke-width="3"/><path d="M0 0L25 16M25 0L0 16" stroke="#c8102e" stroke-width="1"/><path d="M12.5 0V16M0 8H25" stroke="#fff" stroke-width="5"/><path d="M12.5 0V16M0 8H25" stroke="#c8102e" stroke-width="3"/></svg>
  </div>
  <div class="chat">Launch Chat
    <svg width="28" height="22" viewBox="0 0 28 22"><ellipse cx="14" cy="9" rx="13" ry="9" fill="#f5b21a"/><path d="M8 15L5 22L14 17Z" fill="#f5b21a"/></svg>
  </div>
</header>

<main class="main">
  <section class="event" role="img" aria-label="Photo of a DJ with headphones at the decks in a blue-lit club">
    <div class="event-title">Up &amp; Coming Event</div>
    <div class="event-sub">This would be a sub description of the up and coming event</div>
    <div class="event-more">MORE INFO &#9656;</div>
    <div class="dots"><span></span><span></span><span></span><span></span><span></span><span class="on"></span><span></span></div>
  </section>

  <section class="member">
    <h2>MEMBER LOGIN</h2>
    <div class="field-label">Email</div><span class="field"></span>
    <div class="field-label" style="margin-top:10px">Password</div><span class="field"></span>
    <div class="login-row"><span>Forgot your Password?</span><span class="btn-small">LOGIN</span></div>
    <div class="btn-social"><span class="sq"></span>Connect using<b>Chatterloop</b></div>
    <div class="btn-signup">SIGN UP NOW, ITS FREE!</div>
  </section>

  <section class="about">
    <h1>About <b>ZOLNA</b> Radio</h1>
    <p>Lorem ipsum dolor sit amet, consectetur adipisicing elit, sed do eiusmod tempor incididunt ut labore et do lore magna aliqua. Ut enim ad minim veniam, quis nostrud exercitation ullamco laboris nisi ut aliquip ex ea commodo consequat. Duis aute irure dolor in reprehenderit in voluptate velit esse cillum dolore eu fugiat nulla pariatur. Excepteur sint occaecat cupidatat non proident, sunt in culpa qui officia deserunt mollit anim id est laborum. Lorem ipsum dolor sit amet, consectetur adipisicing elit, sed do eiusmod tempor incididunt ut labore et dolore magna aliqua. Ut enim ad minim veniam, quis nostrud exercitation ullamco laboris nisex</p>
  </section>
  <div class="contact">CONTACT US: <a href="mailto:contact@zolnaradio.com">contact@zolnaradio.com</a></div>

  <div class="compat"><span class="y">ZOLNA</span> Radio is now <b>TabQuill</b> &amp; <b>TuneBrick</b> Compatible</div>
  <div class="compat-more">MORE INFO <svg width="14" height="14" viewBox="0 0 14 14"><circle cx="7" cy="7" r="7" fill="#f5b21a"/><path d="M5 3.5L10 7L5 10.5Z" fill="#000"/></svg></div>

  <section class="side">
    <h2>REQUEST A SONG</h2>
    <p>Submit a song and we will do our best to have it played on the air!</p>
    <div class="form-row"><span class="field"></span><span class="btn-small">SUBMIT</span></div>
    <h2 class="second">SEND THIS PAGE TO A FRIEND</h2>
    <p>Tell your friends know about Zolna Radio!</p>
    <div class="form-row"><span class="field"></span><span class="btn-small">SUBMIT</span></div>
  </section>
</main>

<footer class="footer">
  <span class="follow">FOLLOW US:</span>
  <span class="wordmark">chirpline</span>
  <span class="wordmark" style="margin-left:12px">chatterloop</span>
  <div class="shares">
    <div class="share"><span class="b">Like</span><span class="n">1K</span></div>
    <div class="share"><span class="b">Chirp</span><span class="n">2,242</span></div>
    <div class="share"><span class="b orange">Share</span><span class="n">1.3K</span></div>
  </div>
</footer>
</body>
</html>
```